Mesa Copperline Distributors Sales Training

I need a job posting flyer for a hands on Sales Training positions in the electrical distribution market of Phoenix, Arizona. The flyer will be posted on college campuses to recruit new grads for my company. I would like to highlight the benefits of Professional Sales jobs such as a flexible schedule, some out of state travel for training, accelerating career path, and control of earnings based on performance. This is not an everyday sales position, it is professional, complex, and competitive. Applicants should have an entrepreneurial mindset as they will run their accounts as their own business. Mesa Copperline Distributors sells construction electric material to customers in a large scale including electrical conduit, Wire, fittings, high tech lighting and building controls along with other green energy saving devices.
Applicants will send resumes to DaleR@MCDsonoran.com

I have added some pictures that inspire me

Target Market(s)

New college graduates, any bachelors degree

Industry/Entity Type

Electrical Equipment

Font styles to use
Serif

Colors

Designer to choose colors to be used in the design.

Requirements
Must have
• Photos that help show what our industry does, most people are unaware of this industry
• Not wordy, short, get the point across, and where to apply
Nice to have
• creativity and simplicity
Should not have
• too many words

```html
<!DOCTYPE html>
<html lang="en">
<head>
<meta charset="utf-8">
<title>Mesa Copperline Distributors – Sales Training Positions</title>
<link href="https://fonts.googleapis.com/css2?family=Oswald:wght@500;600;700&family=Hind:wght@400;500;600&display=swap" rel="stylesheet">
<style>
  :root {
    --brand-red: #b5191f;
    --banner-red: #a8161c;
    --ink: #141414;
    --paper: #ffffff;
    --muted: #2a2a2a;
  }
  * { margin: 0; padding: 0; box-sizing: border-box; }
  html, body { width: 971px; height: 1200px; overflow: hidden; background: var(--paper); }
  .flyer {
    position: relative;
    width: 971px;
    height: 1200px;
    background: var(--paper);
    font-family: "Hind", sans-serif;
    color: var(--ink);
    overflow: hidden;
  }
  .hero-shapes { position: absolute; left: 0; top: 0; width: 971px; height: 730px; }
  .hiring-banner {
    position: absolute;
    left: 633px; top: 0;
    width: 312px; height: 270px;
  }
  .hiring-title {
    position: absolute;
    left: 633px; top: 44px;
    width: 312px;
    text-align: center;
    font-family: "Oswald", sans-serif;
    font-weight: 700;
    font-size: 84px;
    line-height: 82px;
    letter-spacing: 3px;
    color: var(--paper);
    text-shadow: 0 3px 6px rgba(0,0,0,.35);
  }
  .position-title {
    position: absolute;
    left: 32px; top: 576px;
    font-family: "Oswald", sans-serif;
    font-weight: 600;
    font-size: 42px;
    line-height: 49px;
    color: var(--brand-red);
    text-transform: uppercase;
  }
  .benefits-tab { position: absolute; left: 0; top: 756px; width: 350px; height: 60px; }
  .benefits-label {
    position: absolute;
    left: 32px; top: 762px;
    font-size: 38px;
    line-height: 48px;
    font-weight: 400;
    color: var(--paper);
    letter-spacing: .5px;
  }
  .benefit-list { position: absolute; left: 34px; top: 856px; list-style: none; }
  .benefit-list li {
    display: flex; align-items: center;
    height: 39.5px;
    font-size: 25px;
    font-weight: 500;
    color: var(--ink);
  }
  .benefit-list svg { width: 22px; height: 22px; margin-right: 10px; flex: none; }
  .company-name {
    position: absolute;
    left: 600px; top: 770px;
    width: 330px;
    text-align: center;
    font-family: "Oswald", sans-serif;
    font-weight: 700;
    font-size: 46px;
    line-height: 54px;
    color: var(--ink);
    text-transform: uppercase;
  }
  .company-blurb {
    position: absolute;
    left: 32px; top: 1043px;
    width: 920px;
    font-size: 16.5px;
    line-height: 22px;
    color: var(--muted);
  }
  .apply-bar { position: absolute; left: 0; top: 1114px; width: 971px; height: 86px; }
  .apply-lead {
    position: absolute;
    left: 22px; top: 1138px;
    font-size: 27px;
    font-weight: 600;
    color: var(--paper);
  }
  .apply-contact {
    position: absolute;
    left: 562px; top: 1138px;
    display: flex; align-items: center;
    font-size: 28px;
    font-weight: 600;
    color: var(--paper);
  }
  .apply-contact svg { width: 28px; height: 28px; margin-right: 10px; }
</style>
</head>
<body>
<main class="flyer">

  <svg class="hero-shapes" viewBox="0 0 971 730" aria-hidden="false">
    <defs>
      <linearGradient id="storeTone" x1="0" y1="0" x2="1" y2="1">
        <stop offset="0" stop-color="#6b6f73"/>
        <stop offset=".45" stop-color="#8a7c74"/>
        <stop offset=".75" stop-color="#5a4a48"/>
        <stop offset="1" stop-color="#7a2a2c"/>
      </linearGradient>
      <linearGradient id="bandDark" x1="0" y1="0" x2="1" y2="0">
        <stop offset="0" stop-color="#0c0c0c"/>
        <stop offset=".6" stop-color="#2b2b2b"/>
        <stop offset="1" stop-color="#111"/>
      </linearGradient>
    </defs>
    <polygon role="img" aria-label="Photo of a smiling store worker in an apron holding a screwdriver in front of a wall of tools"
      points="0,0 971,0 971,540 751,622 0,424" fill="url(#storeTone)"/>
    <polygon points="0,424 751,622 971,540 971,562 751,646 0,446" fill="var(--brand-red)"/>
    <polygon points="0,452 751,652 971,570 971,626 751,715 0,518" fill="url(#bandDark)"/>
  </svg>

  <svg class="hiring-banner" viewBox="0 0 312 270" aria-hidden="true">
    <polygon points="0,0 312,0 312,270 156,249 0,270" fill="var(--paper)"/>
    <polygon points="4,0 308,0 308,262 156,242 4,262" fill="var(--banner-red)"/>
  </svg>
  <h1 class="hiring-title">WE'RE<br>HIRING</h1>

  <h2 class="position-title">Sales<br>Training<br>Positions</h2>

  <svg class="benefits-tab" viewBox="0 0 350 60" aria-hidden="true">
    <polygon points="0,0 336,0 350,60 0,60" fill="var(--ink)"/>
  </svg>
  <h3 class="benefits-label">BENEFITS</h3>

  <ul class="benefit-list">
    <li><svg viewBox="0 0 22 22"><circle cx="11" cy="11" r="10" fill="var(--ink)"/><path d="M6 11.5l3.2 3.2L16 8" stroke="#fff" stroke-width="2.4" fill="none"/></svg>Flexible schedule</li>
    <li><svg viewBox="0 0 22 22"><circle cx="11" cy="11" r="10" fill="var(--ink)"/><path d="M6 11.5l3.2 3.2L16 8" stroke="#fff" stroke-width="2.4" fill="none"/></svg>Some out of state travel for training</li>
    <li><svg viewBox="0 0 22 22"><circle cx="11" cy="11" r="10" fill="var(--ink)"/><path d="M6 11.5l3.2 3.2L16 8" stroke="#fff" stroke-width="2.4" fill="none"/></svg>Accelerating career path</li>
    <li><svg viewBox="0 0 22 22"><circle cx="11" cy="11" r="10" fill="var(--ink)"/><path d="M6 11.5l3.2 3.2L16 8" stroke="#fff" stroke-width="2.4" fill="none"/></svg>Control of earnings based on Performance</li>
  </ul>

  <p class="company-name">Mesa Copperline<br>Distributors</p>

  <p class="company-blurb">Mesa Copperline Distributors sells construction electric material to customers in a large scale including: electrical conduit, wire, fittings, high tech lighting and building controls along with other green energy saving devices.</p>

  <svg class="apply-bar" viewBox="0 0 971 86" aria-hidden="true">
    <defs>
      <linearGradient id="barDark" x1="0" y1="0" x2="1" y2="0">
        <stop offset="0" stop-color="#0d0d0d"/>
        <stop offset=".5" stop-color="#2e2e2e"/>
        <stop offset="1" stop-color="#121212"/>
      </linearGradient>
    </defs>
    <rect width="971" height="86" fill="url(#barDark)"/>
    <polygon points="0,0 498,0 470,86 0,86" fill="var(--paper)"/>
    <polygon points="0,0 492,0 464,86 0,86" fill="var(--brand-red)"/>
  </svg>
  <p class="apply-lead">Applicants will send resumes to</p>
  <p class="apply-contact">
    <svg viewBox="0 0 28 28" aria-hidden="true"><circle cx="14" cy="14" r="13" fill="var(--brand-red)"/><rect x="7" y="9" width="14" height="10" rx="1" fill="#fff"/><path d="M7.5 9.5L14 15l6.5-5.5" stroke="var(--brand-red)" stroke-width="1.6" fill="none"/></svg>
    DaleR@MCDsonoran.com
  </p>

</main>
</body>
</html>
```